Business Card design for Founder and CEO of new shoe company

I am looking for a business card design for my new shoe company called Strapwell.

I am launching the company this April. Strapwell shoes offers slip-on athletic and casual style shoes for men and women. The unique selling point of the brand is that all of our shoe exist without shoelaces. I have included a link to the website to offer additional information about the company, see product images, and gain inspiration for the design. You can use the store owner password "Strapwell" to access the website.

www.Strapwell.example

Thanks,
Dan Hollis

Target Market(s)

Active Men and Women ages 16-45

Industry/Entity Type

Business

Contact Information for Business Card

Dan Hollis
Founder and CEO
www.Strapwell.example
danhollis@Strapwell.example
888-555-0187 / 888-5STRAPW
Strapwell, LLC
2284 N Tamsin Ave
Chicago, IL 60699

Requirements
Must have
• Be able to quickly and easily tell that Strapwell is a shoe company from the business card

```html
<!DOCTYPE html>
<html lang="en">
<head>
<meta charset="utf-8">
<title>Strapwell Business Card</title>
<link href="https://fonts.googleapis.com/css2?family=Open+Sans:wght@400;700&display=swap" rel="stylesheet">
<style>
  :root {
    --backdrop: #a3a1a2;
    --paper: #fbfbfb;
    --ink: #1b1b1b;
    --ink-soft: #2c2c2c;
    --band: #1d1f22;
    --floor-top: #9a9ca0;
    --floor-bottom: #3d3f44;
    --shoe-blue: #1e9ee0;
    --shoe-shade: #e9e9ea;
    --white: #ffffff;
  }
  * { margin: 0; padding: 0; box-sizing: border-box; }
  html, body {
    width: 1200px; height: 1200px; overflow: hidden;
    background: var(--backdrop);
    font-family: "Open Sans", Arial, sans-serif;
  }
  .canvas { position: relative; width: 1200px; height: 1200px; }

  .card {
    position: absolute;
    width: 713px; height: 418px;
    background: var(--paper);
    overflow: hidden;
  }

  /* Front */
  .card-front { left: 238px; top: 119px; }
  .front-artwork {
    position: absolute; left: 40px; top: 50px; width: 640px; height: 330px;
    background: radial-gradient(ellipse at 55% 55%, var(--shoe-shade) 0%, rgba(233,233,234,0) 70%);
  }
  .front-wordmark {
    position: absolute; left: 0; right: 0; top: 160px;
    display: flex; align-items: center; justify-content: center; gap: 22px;
  }
  .wordmark-square {
    width: 46px; height: 46px; background: var(--ink);
  }
  .wordmark-text {
    font-size: 72px; font-weight: 400; color: var(--ink); letter-spacing: 1px; line-height: 1;
  }
  .front-band {
    position: absolute; left: 0; bottom: 0; width: 100%; height: 24px; background: var(--band);
  }

  /* Back */
  .card-back { left: 230px; top: 645px; }
  .person { position: absolute; left: 61px; top: 66px; }
  .person-name { font-size: 26px; font-weight: 700; color: var(--ink); line-height: 1.2; }
  .person-title { font-size: 16px; color: var(--ink-soft); margin-top: 6px; }

  .contact { position: absolute; left: 359px; top: 66px; list-style: none; }
  .contact-item {
    display: flex; align-items: center; gap: 16px;
    font-size: 17px; color: var(--ink-soft); height: 26.5px;
  }
  .contact-item svg { width: 19px; height: 15px; flex: none; }
  .address { position: absolute; left: 359px; top: 156px; font-size: 17px; color: var(--ink-soft); }

  .floor {
    position: absolute; left: 0; bottom: 0; width: 100%; height: 122px;
    background: linear-gradient(180deg, var(--floor-top) 0%, var(--floor-bottom) 100%);
  }
  .product-photo {
    position: absolute; left: 0; top: 195px; width: 280px; height: 140px;
    background: radial-gradient(ellipse at 50% 55%, var(--shoe-blue) 0%, #1780bb 55%, rgba(23,128,187,0) 78%);
  }
  .back-wordmark {
    position: absolute; left: 348px; top: 322px;
    display: flex; align-items: center; gap: 16px;
  }
  .back-wordmark .wordmark-square { width: 30px; height: 30px; background: var(--white); }
  .back-wordmark .wordmark-text { font-size: 46px; color: var(--white); }
</style>
</head>
<body>
<div class="canvas">

  <section class="card card-front">
    <div class="front-artwork" role="img" aria-label="Faint line drawing of a pair of slip-on athletic shoes"></div>
    <div class="front-wordmark">
      <span class="wordmark-square"></span>
      <span class="wordmark-text">Strapwell</span>
    </div>
    <div class="front-band"></div>
  </section>

  <section class="card card-back">
    <div class="person">
      <h1 class="person-name">Dan Hollis</h1>
      <p class="person-title">Founder and CEO</p>
    </div>

    <ul class="contact">
      <li class="contact-item">
        <svg viewBox="0 0 19 15" aria-hidden="true"><path d="M2 5c0-3 15-3 15 0v1.5h-4V5H6v1.5H2z M5 7h9l2 7H3z" fill="var(--ink)"/><circle cx="9.5" cy="10.5" r="2" fill="var(--paper)"/></svg>
        <span>888-555-0187 / 888-5STRAPW</span>
      </li>
      <li class="contact-item">
        <svg viewBox="0 0 19 15" aria-hidden="true"><rect x="2" y="2" width="15" height="11" fill="var(--ink)"/><path d="M2 2l7.5 6L17 2" stroke="var(--paper)" stroke-width="1.4" fill="none"/></svg>
        <span>danhollis@Strapwell.example</span>
      </li>
      <li class="contact-item">
        <svg viewBox="0 0 19 15" aria-hidden="true"><circle cx="9.5" cy="7.5" r="6" fill="var(--ink)"/><path d="M3.5 7.5h12M9.5 1.5v12M9.5 1.5c-3 3-3 9 0 12M9.5 1.5c3 3 3 9 0 12" stroke="var(--paper)" stroke-width="0.9" fill="none"/></svg>
        <span>www.Strapwell.example</span>
      </li>
    </ul>
    <p class="address">2284 N Tamsin Ave Chicago, IL 60699</p>

    <div class="floor"></div>
    <div class="product-photo" role="img" aria-label="Photo of a pair of blue and black slip-on running shoes on a dark floor"></div>
    <div class="back-wordmark">
      <span class="wordmark-square"></span>
      <span class="wordmark-text">Strapwell</span>
    </div>
  </section>

</div>
</body>
</html>
```